Restaurant needs a vertical banner for fried catfish

Our restaurant is looking for an eye-catching 78.75in. x 36in. vertical physical banner ad for our fried catfish. Photos for the fried catfish will be provided as a reference but we will also accept anything similar to the photo. We will be using the following as our receptacle: https://www.plankoria.example/banner-stand/retractable-banner-stands/
The design must incorporate the following flavor texts:
Fried Catfish
Always Fresh!
Made from Scratch
Hand-cut Fillets
The Best Catfish in Texas
Served with fries, hush puppies, and a 32oz fountain drink
Also available by the pound!
The final design should be creative, professional, and eye-catching for customers.
Updates
Colors
Designer to choose colors to be used in the design.
Requirements
Must have
- We are open to any and all design elements, albeit the 'flavor texts' should not overpower, but complement the fried catfish photo. 'Fried Catfish' can be used in lieu of a main title/logo.
Nice to have
- Transparent or textured backgrounds that can encompass any or all part of the banner such as a cutting board, shadows, abstract, etc to show depth are a plus.
- Use of vectors or objects such as ribbons or shapes to encapsulate the 'flavor texts' are also encouraged.

```html
<!DOCTYPE html>
<html lang="en">
<head>
<meta charset="utf-8">
<title>Fried Catfish Vertical Banner</title>
<link rel="stylesheet" href="https://fonts.googleapis.com/css2?family=Yellowtail&family=Oswald:wght@500;700&family=Open+Sans:wght@400;700&display=swap">
<style>
  :root {
    --page: #e4e4e4;
    --wood: #2a2a2a;
    --wood-line: #343434;
    --red: #c8280c;
    --orange: #ef7a1d;
    --yellow: #f7b51d;
    --gold: #f5b820;
    --white: #ffffff;
    --ink-red: #a8230c;
    --flame: #e84a1c;
  }
  html, body {
    margin: 0;
    width: 1200px;
    height: 1200px;
    overflow: hidden;
    background: var(--page);
  }
  .canvas {
    width: 1200px;
    height: 1200px;
    display: flex;
    align-items: center;
    justify-content: center;
  }
  .banner {
    width: 522px;
    height: 1140px;
    display: block;
    box-shadow: 0 6px 18px rgba(0,0,0,.25);
  }
  .title, .script { font-family: "Yellowtail", "Brush Script MT", cursive; font-style: italic; }
  .condensed { font-family: "Oswald", "Arial Narrow", sans-serif; font-weight: 700; }
  .body-copy { font-family: "Open Sans", Arial, sans-serif; }
</style>
</head>
<body>
<main class="canvas">
  <svg class="banner" viewBox="0 0 554 1210" xmlns="http://www.w3.org/2000/svg">
    <defs>
      <pattern id="wood-grain" width="554" height="26" patternUnits="userSpaceOnUse">
        <rect width="554" height="26" fill="var(--wood)"/>
        <rect y="24" width="554" height="2" fill="var(--wood-line)"/>
      </pattern>
      <linearGradient id="silhouette-tone" x1="0" y1="0" x2="1" y2="0">
        <stop offset="0" stop-color="#ffffff" stop-opacity="0.15"/>
        <stop offset="0.45" stop-color="#ffffff" stop-opacity="0.75"/>
        <stop offset="1" stop-color="#ffffff" stop-opacity="0.95"/>
      </linearGradient>
      <linearGradient id="food-tones" x1="0" y1="0" x2="1" y2="1">
        <stop offset="0" stop-color="#d9d2c6"/>
        <stop offset="0.3" stop-color="#c88a3c"/>
        <stop offset="0.6" stop-color="#a8642a"/>
        <stop offset="1" stop-color="#e0b262"/>
      </linearGradient>
      <radialGradient id="tomato-tones" cx="50%" cy="50%" r="50%">
        <stop offset="0" stop-color="#c8281c"/>
        <stop offset="1" stop-color="#2a2a2a" stop-opacity="0"/>
      </radialGradient>
    </defs>

    <rect class="backdrop" width="554" height="1210" fill="url(#wood-grain)"/>
    <rect class="top-band" width="554" height="28" fill="var(--red)"/>

    <!-- fish silhouette area -->
    <rect class="fish-silhouette" x="175" y="222" width="379" height="118" rx="40"
          fill="url(#silhouette-tone)" role="img" aria-label="White catfish silhouette"/>

    <!-- headline -->
    <text class="title" x="30" y="205" transform="rotate(-13 30 205)" font-size="66"
          fill="var(--white)" stroke="var(--red)" stroke-width="4" paint-order="stroke">Fried Catfish!</text>

    <!-- always fresh badge -->
    <g class="fresh-badge">
      <circle cx="78" cy="487" r="92" fill="var(--yellow)" stroke="var(--red)" stroke-width="5"/>
      <text class="condensed" x="78" y="470" text-anchor="middle" font-size="36" fill="var(--ink-red)">ALWAYS</text>
      <text class="condensed" x="78" y="527" text-anchor="middle" font-size="48" fill="var(--flame)">FRESH</text>
    </g>

    <!-- selling points -->
    <g class="selling-points" fill="var(--white)">
      <text class="script" x="196" y="438" font-size="34">Made from Scratch</text>
      <text class="script" x="202" y="484" font-size="34">Hand-cut Fillets</text>
      <text class="body-copy" x="203" y="521" font-size="15.5">Served with fries, hush puppies,</text>
      <text class="body-copy" x="203" y="543" font-size="15.5">and a 32oz fountain drink</text>
    </g>

    <!-- food photo area -->
    <g class="food-photo" role="img" aria-label="Plate of fried catfish fillets with fries, hush puppies, tartar sauce and cherry tomatoes">
      <ellipse cx="55" cy="810" rx="55" ry="110" fill="url(#tomato-tones)"/>
      <rect x="85" y="628" width="469" height="330" rx="150" fill="url(#food-tones)"/>
    </g>

    <!-- ribbons -->
    <polygon class="ribbon-orange" points="0,1022 554,872 554,962 0,1112" fill="var(--orange)"/>
    <polygon class="ribbon-red" points="0,1112 554,962 554,1018 0,1210" fill="var(--red)"/>

    <g class="ribbon-copy" transform="rotate(-15 20 1085)">
      <text class="condensed" x="22" y="1080" font-size="44" fill="var(--white)">THE BEST CATFISH IN TEXAS!</text>
      <text class="body-copy" x="160" y="1106" font-size="19" fill="var(--white)">Also available by the pound!</text>
    </g>

    <!-- website -->
    <g class="website" transform="rotate(-15 60 1180)">
      <circle cx="68" cy="1172" r="9" fill="none" stroke="var(--white)" stroke-width="2"/>
      <ellipse cx="68" cy="1172" rx="4" ry="9" fill="none" stroke="var(--white)" stroke-width="1.5"/>
      <line x1="59" y1="1172" x2="77" y2="1172" stroke="var(--white)" stroke-width="1.5"/>
      <text class="body-copy" x="84" y="1180" font-size="22" font-weight="700" fill="var(--white)">www.crispfillet.example</text>
    </g>

    <!-- phone -->
    <g class="phone">
      <circle cx="518" cy="1124" r="17" fill="var(--red)"/>
      <path d="M511 1116 q-3 3 0 9 q5 9 13 12 q4 1 6 -2 l-4 -4 q-2 1 -3 0 q-5 -3 -7 -8 q0 -1 1 -3 z" fill="var(--white)"/>
      <text class="condensed" x="536" y="1195" text-anchor="end" font-size="44" font-weight="500" fill="var(--gold)">555 010 321</text>
    </g>
  </svg>
</main>
</body>
</html>
```